Pflegedienst sucht Flyerdesign
Zielgruppe
Wir sind ein ambulanter Pflegedienst und betreuen ca. 200 Patienten in ländlicher Region. Unsere Zielgruppe sind Pflegebedürftige aus altersbedingten Gründen oder nach Krankenhausaufenthalten. Wir setzen auf Qualität, Zuverlässigkeit, Exklusivität.
Aufgabenstellung
DIN lang Flyer. Wir werben ganz bewußt nicht mit Bildern von Senioren oder alten Menschen, weil das fast alle Pflegedienste tun. Daher setzen wir eher auf Motive aus unserer Urlaubsregion: Strand, Meer...
Unseren Firmen-Vebo hätten wir gern als Fotoausschnitt ohne Hintergund mit dabei.
Und einen Kartenausschnitt mit unserem Einzugsgebiet fänden wir toll. Dies umfasst ca. 15 km um Laboe und Heikendorf folgende Orte: Stein, Wendtorf, Probsteierhagen, Schönkirchen und Mönkeberg.

```html
<!DOCTYPE html>
<html lang="de">
<head>
<meta charset="utf-8">
<title>Flyer – Ambulante Krankenpflege Kliffhagen &amp; Dünenfeld</title>
<link rel="stylesheet" href="https://fonts.googleapis.com/css2?family=PT+Sans:wght@400;700&display=swap">
<style>
  :root{
    --stage:#bcd1d8;
    --paper:#ffffff;
    --ink:#7f9598;
    --ink-strong:#6d8487;
    --accent:#a8145c;
    --deco:#94a6a9;
    --sky-top:#2f86cf;
    --sky-low:#8cc3e6;
    --sand:#ece8df;
    --car:#8c969d;
    --map-sea:#8ecfcb;
    --map-land:#eeece4;
  }
  *{margin:0;padding:0;box-sizing:border-box}
  html,body{width:1200px;height:960px;overflow:hidden}
  body{background:var(--stage);font-family:"PT Sans",sans-serif;color:var(--ink);position:relative}
  .card{position:absolute;left:160px;width:880px;height:430px;background:var(--paper);box-shadow:0 10px 24px rgba(40,70,80,.25)}
  .card--front{top:35px}
  .card--back{top:495px}
  .abs{position:absolute}

  .logo{position:absolute;text-align:right;text-transform:uppercase;color:var(--ink);font-weight:400;line-height:1.12;letter-spacing:.01em}
  .logo__dot{position:absolute;border-radius:50%;background:var(--accent)}

  .card--front .logo{right:106px;top:34px;font-size:29px}
  .card--front .logo__dot{left:783px;top:55px;width:64px;height:64px}

  .beach{left:81px;top:79px;width:289px;height:282px;
    background:linear-gradient(180deg,var(--sky-top) 0%,var(--sky-low) 40%,#3d8fb8 42%,#2f7fa8 52%,var(--sand) 53%,#f3f1ec 100%)}
  .deco-square{background:var(--deco);border-radius:8px;width:72px;height:72px}
  .card--front .deco-square{left:50px;top:315px}

  .tagline{right:93px;top:160px;text-align:right;font-size:14.5px;line-height:1.25}
  .tagline strong{color:var(--ink-strong)}

  .vehicle{left:425px;top:240px;width:262px;height:115px;border-radius:40px 60px 24px 24px;
    background:linear-gradient(180deg,#aab3b9 0%,var(--car) 55%,#5e676d 100%)}

  .services{top:46px;font-size:13.5px;line-height:1.35}
  .services--a{left:37px;top:52px}
  .services--b{left:223px}
  .services--c{left:410px;top:42px}
  .card--back .logo{right:92px;top:38px;font-size:20px}
  .card--back .logo__dot{left:795px;top:23px;width:40px;height:40px}
  .divider{left:37px;top:111px;width:801px;border-top:1px dotted var(--ink)}

  .map{left:65px;top:178px;width:197px;height:194px;
    background:linear-gradient(120deg,var(--map-sea) 0%,var(--map-sea) 32%,var(--map-land) 33%,#e6e4da 100%)}
  .card--back .deco-square{left:37px;top:318px}

  .company{left:316px;top:178px;color:var(--accent);font-size:15px}
  .label{font-size:14px;letter-spacing:.12em;text-transform:uppercase}
  .address{font-size:14.5px;line-height:1.22}
  .hq-label{left:316px;top:214px}
  .hq{left:316px;top:250px}
  .web{left:316px;top:338px;font-size:14.5px;line-height:1.22;letter-spacing:.04em}
  .branch-label{left:615px;top:214px}
  .branch{left:615px;top:250px}
  .oncall{left:615px;top:353px;color:var(--accent);font-size:14.5px}
</style>
</head>
<body>

<section class="card card--front">
  <div class="abs beach" role="img" aria-label="Foto: Sandstrand mit Ostsee und blauem Himmel"></div>
  <div class="abs deco-square"></div>

  <div class="logo">Ambulante Krankenpflege<br>Kliffhagen &amp; Dünenfeld</div>
  <div class="logo__dot"></div>

  <p class="abs tagline">Ihr Premiumdienst in der Region<br>von <strong>Mensch zu Mensch</strong> seit über 20 Jahren</p>

  <div class="abs vehicle" role="img" aria-label="Freigestelltes Foto des grauen Firmen-Vebo mit Beschriftung des Pflegedienstes"></div>
</section>

<section class="card card--back">
  <ul class="abs services services--a" style="list-style:none">
    <li>Häusliche Pflege</li><li>Pflegeberatung</li><li>Demenzbetreuung</li>
  </ul>
  <ul class="abs services services--b" style="list-style:none">
    <li>Aktivierende Beschäftigung</li><li>Entlastung im Haushalt</li><li>Palliativpflege</li>
  </ul>
  <ul class="abs services services--c" style="list-style:none">
    <li>Sterbebegleitung</li><li>24 h Rufbereitschaft</li>
  </ul>

  <div class="logo">Ambulante Krankenpflege<br>Kliffhagen &amp; Dünenfeld</div>
  <div class="logo__dot"></div>

  <div class="abs divider"></div>

  <div class="abs map" role="img" aria-label="Kartenausschnitt des Einzugsgebiets an der Förde mit markierter Gebietsgrenze"></div>
  <div class="abs deco-square"></div>

  <p class="abs company">Ambulante Krankenpflege Kliffhagen GmbH</p>

  <p class="abs label hq-label">Hauptsitz:</p>
  <p class="abs address hq">Lindenweg 7<br>24999 Kliffhagen<br>TEL 04399 – 12 30<br>FAX 04399- 45 67</p>
  <p class="abs web">info@pflegedienst-kliffhagen.de<br>www.pflegedienst-kliffhagen.de</p>

  <p class="abs label branch-label">Niederlassung:</p>
  <p class="abs address branch">Mühlenstraße 12<br>24998 Dünenfeld<br>TEL 0499- 21 43 65 10<br>FAX 0499- 21 43 65 11</p>
  <p class="abs oncall">Rufbereitschaft 0170 – 00 98 765</p>
</section>

</body>
</html>
```